Business cards for Remote DBA team

Business cards for team offering database administration, consultation, machine learning and AI services. As of now team is using both
www.fenrowlabs.cz and www.quillbarkgroup.cz URLs

Target Market(s)

IT managers

Industry/Entity Type

It Professional

Contact Information for Business Card

Should include logo
name, email, phone, twitter tag

Font styles to use
Sans Serif

Colors

Designer to choose colors to be used in the design.

```html
<!DOCTYPE html>
<html lang="en">
<head>
<meta charset="utf-8">
<title>Fenrow Labs – Business Card</title>
<link rel="stylesheet" href="https://fonts.googleapis.com/css2?family=Montserrat:wght@400;700;800&family=Arimo:wght@400&display=swap">
<style>
  :root {
    --page-bg: #d9d6d1;
    --card-bg: #f4f6f8;
    --card-edge: #e3e7ec;
    --brand-blue: #1b5a9c;
    --deep-blue: #114a86;
    --soft-blue: #c9d6e4;
    --text-grey: #5d6166;
    --contact-tint: #e6dcc8;
  }
  * { margin: 0; padding: 0; box-sizing: border-box; }
  html, body { width: 1200px; height: 970px; overflow: hidden; background: var(--page-bg); }
  .canvas { position: relative; width: 1200px; height: 970px; }
  .card {
    position: absolute; left: 80px; top: 190px; width: 1040px; height: 590px;
    border-radius: 30px; overflow: hidden;
    background: linear-gradient(160deg, #ffffff 0%, var(--card-bg) 55%, var(--card-edge) 100%);
    box-shadow: 0 18px 40px rgba(0,0,0,0.18);
  }
  .wave-area {
    position: absolute; left: 0; right: 0; bottom: 0; height: 260px;
    background: linear-gradient(100deg, var(--soft-blue) 0%, var(--brand-blue) 45%, var(--deep-blue) 100%);
  }
  .brand { position: absolute; left: 80px; top: 118px; display: flex; align-items: center; gap: 26px; }
  .brand-dot { width: 92px; height: 92px; border-radius: 50%; background: var(--brand-blue); flex: none; }
  .brand-name {
    font-family: "Montserrat", sans-serif; font-weight: 800; color: var(--brand-blue);
    font-size: 52px; line-height: 0.98; letter-spacing: 0.5px;
  }
  .holder { position: absolute; right: 52px; top: 70px; text-align: right; }
  .holder-name {
    font-family: "Montserrat", sans-serif; font-weight: 800; font-size: 31px;
    letter-spacing: 1.5px; color: var(--deep-blue);
  }
  .holder-role { font-family: "Arimo", sans-serif; font-size: 24px; color: var(--text-grey); margin-top: 2px; }
  .contacts { position: absolute; right: 50px; top: 376px; list-style: none; }
  .contact-line {
    display: flex; justify-content: flex-end; align-items: center; gap: 14px;
    height: 35px; font-family: "Arimo", sans-serif; font-size: 23px; letter-spacing: 0.4px;
    color: var(--contact-tint);
  }
  .contact-icon { width: 32px; height: 32px; flex: none; }
</style>
</head>
<body>
<main class="canvas">
  <section class="card">
    <div class="wave-area" role="img" aria-label="Decorative flowing wave artwork in blue, grey and blush tones"></div>

    <div class="brand">
      <span class="brand-dot"></span>
      <div class="brand-name">FENROW<br>LABS</div>
    </div>

    <div class="holder">
      <div class="holder-name">PETRA HALVIK</div>
      <div class="holder-role">Founder</div>
    </div>

    <ul class="contacts">
      <li class="contact-line">420.614.2087
        <svg class="contact-icon" viewBox="0 0 32 32" aria-hidden="true"><circle cx="16" cy="16" r="14" fill="none" stroke="var(--contact-tint)" stroke-width="2.5"/><path d="M11 9 l3 0 l1.5 4 l-2 1.5 a9 9 0 0 0 4 4 l1.5 -2 l4 1.5 l0 3 a2 2 0 0 1 -2 2 a13 13 0 0 1 -12 -12 a2 2 0 0 1 2 -2z" fill="var(--contact-tint)"/></svg>
      </li>
      <li class="contact-line">hello@fenrowlabs.cz
        <svg class="contact-icon" viewBox="0 0 32 32" aria-hidden="true"><circle cx="16" cy="16" r="14" fill="none" stroke="var(--contact-tint)" stroke-width="2.5"/><rect x="9" y="11" width="14" height="10" rx="1" fill="none" stroke="var(--contact-tint)" stroke-width="2"/><path d="M9 11 l7 6 l7 -6" fill="none" stroke="var(--contact-tint)" stroke-width="2"/></svg>
      </li>
      <li class="contact-line">www.fenrowlabs.cz
        <svg class="contact-icon" viewBox="0 0 32 32" aria-hidden="true"><circle cx="16" cy="16" r="14" fill="none" stroke="var(--contact-tint)" stroke-width="2.5"/><circle cx="16" cy="16" r="8" fill="none" stroke="var(--contact-tint)" stroke-width="1.8"/><ellipse cx="16" cy="16" rx="3.5" ry="8" fill="none" stroke="var(--contact-tint)" stroke-width="1.5"/><path d="M8 16 h16" stroke="var(--contact-tint)" stroke-width="1.5"/></svg>
      </li>
      <li class="contact-line">www.quillbarkgroup.cz
        <svg class="contact-icon" viewBox="0 0 32 32" aria-hidden="true"><circle cx="16" cy="16" r="14" fill="none" stroke="var(--contact-tint)" stroke-width="2.5"/><circle cx="16" cy="16" r="8" fill="none" stroke="var(--contact-tint)" stroke-width="1.8"/><ellipse cx="16" cy="16" rx="3.5" ry="8" fill="none" stroke="var(--contact-tint)" stroke-width="1.5"/><path d="M8 16 h16" stroke="var(--contact-tint)" stroke-width="1.5"/></svg>
      </li>
      <li class="contact-line">@fenrowlabs
        <svg class="contact-icon" viewBox="0 0 32 32" aria-hidden="true"><circle cx="16" cy="16" r="14" fill="none" stroke="var(--contact-tint)" stroke-width="2.5"/><circle cx="16" cy="16" r="7" fill="var(--contact-tint)"/></svg>
      </li>
    </ul>
  </section>
</main>
</body>
</html>
```